Re-design of current business cards

We are updating our website with new colors and layout. Would like to re-design our business cards to co-ordinate. See attached pdf with new Brightwell website colors. We would also like to combine our 2 brands on the one business card. Attached is the new design for our Brightwell website, current business cards, which are one sided, brightwell logo in tiff, .ai for fonts. Brightwell logo font is Optimum, Lanterncove website home page image, Lanterncove brand statics for products which includes the logo for this brand.

Lanterncove brand will stay the dark gray on the website. See attached statics for product and website home page.
Updates

The business cards will be 2 sided. Brightwell Brand on one side and Lanterncove Brand on the other. The colors for Brightwell need to follow the color scheme of the brightwell website pdf I uploaded. The colors are a blue, lighter teal blue and white. Lanterncove needs to follow the dark gray color on files uploaded

Target Market(s)

The trade and consumers

Industry/Entity Type

Home Furnishing

Contact Information for Business Card

We are updating our website with new colors and layout. Would like to re-design our business cards to co-ordinate. We would also like to combine our 2 brands onto 1 2 sided business cards.

Requirements
Must have
• Colors that match our new website, see attached image.
• RGB colors
• navy -#152842
• teal - 98aeb9
• The gray color used for Lanterncove brands.
• ll logos and fonts should stay the same.

```html
<!DOCTYPE html>
<html lang="en">
<head>
<meta charset="utf-8">
<title>Brightwell &amp; Lanterncove Business Cards</title>
<link rel="stylesheet" href="https://fonts.googleapis.com/css2?family=Marcellus&family=Montserrat:wght@400;700&family=Roboto+Condensed:wght@300;400&display=swap">
<style>
  :root {
    --navy: #152842;
    --teal: #98aeb9;
    --paper: #f7f8f9;
    --lantern-gray: #6a6a6b;
    --lantern-ink: #dedede;
    --backdrop: #eceef0;
    --body-ink: #2b3442;
  }
  * { box-sizing: border-box; margin: 0; padding: 0; }
  html, body { width: 1200px; height: 720px; overflow: hidden; }
  body {
    background: var(--backdrop);
    display: flex;
    align-items: center;
    justify-content: center;
    gap: 40px;
  }
  .card {
    position: relative;
    width: 540px;
    height: 309px;
    overflow: hidden;
    box-shadow: 0 2px 8px rgba(0,0,0,0.12);
  }

  /* Lanterncove side */
  .card--lanterncove {
    background: var(--lantern-gray);
    color: var(--lantern-ink);
    display: flex;
    flex-direction: column;
    align-items: center;
    justify-content: center;
    text-align: center;
  }
  .lanterncove-name {
    font-family: "Marcellus", serif;
    font-size: 48px;
    letter-spacing: 1px;
    font-weight: 400;
  }
  .lanterncove-tagline {
    margin-top: 30px;
    font-family: "Roboto Condensed", sans-serif;
    font-weight: 300;
    font-size: 22px;
  }
  .lanterncove-url {
    margin-top: 18px;
    font-family: "Roboto Condensed", sans-serif;
    font-weight: 300;
    font-size: 13px;
    letter-spacing: 0.3px;
  }

  /* Brightwell side */
  .card--brightwell { background: var(--paper); color: var(--body-ink); }
  .band-teal {
    position: absolute; left: 0; top: 0;
    width: 100%; height: 72px;
    background: var(--teal);
  }
  .band-navy {
    position: absolute; left: 0; top: 78px;
    width: 100%; height: 20px;
    background: var(--navy);
    color: #fff;
    font-family: "Roboto Condensed", sans-serif;
    font-size: 12px;
    line-height: 20px;
    text-align: right;
    padding-right: 18px;
  }
  .band-navy strong { font-weight: 400; letter-spacing: 0.3px; }
  .brand-mark {
    position: absolute; left: 46px; top: 56px;
    width: 62px; height: 62px;
    border-radius: 50%;
    background: var(--navy);
    border: 5px solid var(--paper);
  }
  .brand-name {
    position: absolute; left: 46px; top: 122px;
    font-family: "Marcellus", serif;
    font-size: 34px;
    color: #111;
    letter-spacing: 0.5px;
  }
  .brand-url {
    position: absolute; left: 118px; top: 164px;
    font-family: "Montserrat", sans-serif;
    font-size: 11px;
    color: #333;
  }
  .person {
    position: absolute; left: 46px; top: 214px;
  }
  .person-name {
    font-family: "Montserrat", sans-serif;
    font-weight: 700;
    font-size: 19px;
    color: var(--navy);
    letter-spacing: 0.4px;
  }
  .person-title {
    margin-top: 4px;
    font-family: "Montserrat", sans-serif;
    font-size: 10.5px;
    color: #333;
    letter-spacing: 0.3px;
  }
  .contact {
    position: absolute; right: 20px; top: 132px;
    list-style: none;
    font-family: "Montserrat", sans-serif;
    font-size: 10px;
    color: #333;
    letter-spacing: 0.2px;
  }
  .contact-item {
    display: flex;
    align-items: center;
    justify-content: flex-end;
    gap: 10px;
    margin-bottom: 12px;
    text-align: right;
    line-height: 1.35;
  }
  .contact-phones { display: flex; align-items: center; gap: 8px; }
  .icon { width: 14px; height: 14px; fill: var(--teal); flex: none; }
</style>
</head>
<body>

  <section class="card card--lanterncove" aria-label="Lanterncove side">
    <h1 class="lanterncove-name">LANTERNCOVE</h1>
    <p class="lanterncove-tagline">Discover the luxury of home.</p>
    <p class="lanterncove-url">www.lanterncovebybrightwell.com</p>
  </section>

  <section class="card card--brightwell" aria-label="Brightwell side">
    <div class="band-teal"></div>
    <div class="band-navy">WWW.<strong>BRIGHTWELL</strong>.COM</div>
    <div class="brand-mark"></div>
    <h1 class="brand-name">BRIGHTWELL</h1>
    <p class="brand-url">www.brightwell.com</p>

    <div class="person">
      <h2 class="person-name">DANA WHITFORD</h2>
      <p class="person-title">GRAPHICS/PHOTOGRAPHY DESIGNER</p>
    </div>

    <ul class="contact">
      <li class="contact-item">
        <span>PO BOX 214/1180 MEADOW RIDGE RD<br>FAIRHAVEN, OHIO 45001</span>
        <svg class="icon" viewBox="0 0 24 24" aria-hidden="true"><path d="M12 2a7 7 0 0 0-7 7c0 5 7 13 7 13s7-8 7-13a7 7 0 0 0-7-7zm0 9.5A2.5 2.5 0 1 1 12 6.5a2.5 2.5 0 0 1 0 5z"/></svg>
      </li>
      <li class="contact-item">
        <span class="contact-phones">
          555.210.4417
          <svg class="icon" viewBox="0 0 24 24" aria-hidden="true"><path d="M6.6 10.8a15 15 0 0 0 6.6 6.6l2.2-2.2a1 1 0 0 1 1-.25 11.4 11.4 0 0 0 3.6.57 1 1 0 0 1 1 1V20a1 1 0 0 1-1 1A17 17 0 0 1 3 4a1 1 0 0 1 1-1h3.5a1 1 0 0 1 1 1c0 1.25.2 2.45.57 3.57a1 1 0 0 1-.25 1z"/></svg>
          555.210.4418
        </span>
        <svg class="icon" viewBox="0 0 24 24" aria-hidden="true"><path d="M6 3h12v5H6zM4 9h16a2 2 0 0 1 2 2v6h-4v4H6v-4H2v-6a2 2 0 0 1 2-2zm4 7v3h8v-3z"/></svg>
      </li>
      <li class="contact-item">
        <span>DWHITFORD@BRIGHTWELL.COM</span>
        <svg class="icon" viewBox="0 0 24 24" aria-hidden="true"><path d="M3 5h18v14H3zm2 2v.5l7 5 7-5V7z"/></svg>
      </li>
    </ul>
  </section>

</body>
</html>
```